Home page makeover

Take my existing home page, www.maplecrestharborline.com and redesign layout to look more current considering today's touch design prevalence.
Reuse existing elements or suggest improved ones if available.
I generally have average CSS and HTML skills using div containers, defining lists and using columns to create the code to support the layout.
Updates
Just wanted to send out a quick message to thank all of you for your submissions. Many of you offered nice designs, but unfortunately could only choose one.
Target Market(s)
Generally targeting individuals with some assets for retirement. Basically your average working professional or business owner.
Industry/Entity Type
It Support
Look and feel
Each slider illustrates characteristics of the customer's brand and the style your logo design should communicate.

```html
<!DOCTYPE html>
<html lang="en">
<head>
<meta charset="utf-8">
<title>Maplecrest Harborline — Retirement Plans</title>
<link href="https://fonts.googleapis.com/css2?family=Jost:wght@400;500&family=Arimo:ital,wght@0,400;0,700;1,400&display=swap" rel="stylesheet">
<style>
:root{
  --green:#8cc63f;
  --green-dark:#2e6b1f;
  --grey-btn:#8a8a8a;
  --ink:#333;
  --text:#555;
  --muted:#888;
  --band:#f3f3f3;
  --orange:#ff9900;
  --footer:#333;
  --white:#fff;
}
*{box-sizing:border-box;margin:0;padding:0}
html,body{width:787px;height:1200px;overflow:hidden;background:var(--white)}
body{font-family:"Arimo",Arial,sans-serif;color:var(--text);font-size:9px;position:relative}
.heading{font-family:"Jost",sans-serif;font-weight:400;color:var(--ink)}
.container{position:absolute;left:99px;width:590px}

/* header */
.site-header{position:absolute;top:0;left:0;width:787px;height:80px}
.brand{position:absolute;left:99px;top:24px;display:flex;align-items:center;gap:7px}
.brand-mark{width:14px;height:14px;background:var(--green-dark)}
.brand-name{font-family:"Jost",sans-serif;font-size:17px;font-weight:500;color:var(--green-dark)}
.account{position:absolute;right:99px;top:11px;display:flex;gap:8px}
.btn{display:block;height:18px;line-height:18px;padding:0 11px;font-size:9px;color:var(--white);border-radius:2px}
.btn-signin{background:var(--green)}
.btn-signup{background:var(--grey-btn)}
.main-nav{position:absolute;right:99px;top:48px;display:flex;gap:27px;font-size:10.5px;color:#444}

/* hero */
.hero{position:absolute;top:80px;left:0;width:787px;height:305px;
  background:linear-gradient(180deg,#cfd8de 0%,#a9b3b5 18%,#6c9a3e 34%,#5e9a2a 60%,#8aae3a 85%,#b0a448 100%)}
.hero-copy{position:absolute;top:140px;width:100%;text-align:center;color:var(--white)}
.hero-title{font-family:"Jost",sans-serif;font-weight:500;font-size:21px;letter-spacing:.3px}
.hero-text{font-size:9.5px;line-height:12px;margin-top:2px}
.hero-arrow{position:absolute;top:128px}
.hero-arrow.prev{left:76px}.hero-arrow.next{right:76px}

/* steps */
.steps{position:absolute;top:385px;left:0;width:787px;height:155px;background:var(--band)}
.steps .container{top:18px;display:flex;justify-content:space-between}
.step{width:170px}
.step-title{font-size:15px;line-height:15px;color:#222}
.step-note{font-style:italic;font-size:7px;color:var(--muted);margin:2px 0 4px}
.step-photo{width:170px;height:82px;border:2px solid var(--white);box-shadow:0 0 2px rgba(0,0,0,.2)}
.photo-money{background:linear-gradient(135deg,#b8b8b0,#e2ddd4 50%,#9a9c92)}
.photo-laptop{background:linear-gradient(135deg,#2a2a2a,#6a6a6a 55%,#e8e8e8)}
.photo-hammock{background:linear-gradient(180deg,#8bb0cc,#b9cfe0 45%,#a98a5e 70%,#e8e4dc)}

/* features */
.section-title{font-size:19px;text-align:center;letter-spacing:.5px}
.features{position:absolute;top:540px;left:0;width:787px;height:199px}
.features .section-title{margin-top:21px}
.feature-grid{top:62px;display:grid;grid-template-columns:280px 270px;column-gap:43px;row-gap:16px}
.feature{display:flex;gap:7px}
.feature-icon{flex:none;width:29px;height:29px;border-radius:50%;background:var(--green);display:flex;align-items:center;justify-content:center}
.feature p{font-size:8.5px;line-height:12.5px;color:#666}

/* signup + video */
.join{position:absolute;top:739px;left:0;width:787px;height:229px;background:var(--band)}
.signup-card{position:absolute;left:127px;top:30px;width:184px}
.signup-head{background:#999;color:var(--white);text-align:center;font-family:"Jost",sans-serif;font-size:14px;height:30px;line-height:30px;letter-spacing:.5px}
.signup-body{background:#ddd;padding:11px 11px 9px}
.field{height:22px;background:var(--white);border:1px solid #ccc;margin-bottom:7px;padding-left:6px;line-height:21px;font-size:10px;color:#888}
.submit{height:22px;background:var(--orange);color:var(--white);text-align:center;line-height:22px;font-size:10px}
.signup-perks{background:var(--green);color:var(--white);list-style:none;padding:5px 11px;font-size:7.5px;line-height:17px}
.signup-perks li{display:flex;align-items:center;gap:5px}
.video{position:absolute;left:428px;top:31px;width:251px;height:168px;box-shadow:0 1px 4px rgba(0,0,0,.3)}
.video-frame{height:152px;background:linear-gradient(180deg,#9cc3e0 0%,#7aa8cc 35%,#3a6a8a 45%,#6f8c4a 70%,#4f6e2a 100%);position:relative}
.video-play{position:absolute;left:110px;top:62px}
.video-bar{height:16px;background:linear-gradient(#e6e6e6,#c8c8c8);display:flex;align-items:center;gap:6px;padding:0 7px;font-size:5px;color:#555}
.track{flex:1;height:4px;background:#777;border-radius:2px;position:relative}
.track::before{content:"";position:absolute;left:0;top:0;height:4px;width:48%;background:#d33;border-radius:2px}
.vol{width:30px;height:4px;background:#555;border-radius:2px}

/* testimonials */
.testimonials{position:absolute;top:968px;left:0;width:787px;height:180px}
.testimonials .section-title{margin-top:20px}
.quote-row{top:63px;display:flex;justify-content:space-between}
.quote{width:172px}
.bubble{position:relative;border:1px solid #ccc;border-radius:4px;padding:13px 9px 9px;font-style:italic;font-size:8.5px;line-height:11px;color:#555;background:var(--white)}
.bubble::after{content:"";position:absolute;left:26px;bottom:-9px;width:12px;height:12px;background:var(--white);border-right:1px solid #ccc;border-bottom:1px solid #ccc;transform:skewY(40deg) rotate(45deg)}
.author{margin:11px 0 0 11px;font-size:8.5px;color:#222}
.author span{color:var(--green)}

/* footer */
.site-footer{position:absolute;top:1148px;left:0;width:787px;height:52px;background:var(--footer);color:var(--white);text-align:center;font-size:8.5px;line-height:15px;padding-top:10px}
</style>
</head>
<body>

<header class="site-header">
  <a class="brand"><span class="brand-mark"></span><span class="brand-name">Maplecrest Harborline</span></a>
  <div class="account"><a class="btn btn-signin">Sign In</a><a class="btn btn-signup">Sign up</a></div>
  <nav class="main-nav"><a>Home</a><a>About us</a><a>Services</a><a>Testimonials</a><a>Contact us</a></nav>
</header>

<section class="hero" role="img" aria-label="Photo of green hills, a mountain village and snowy peaks">
  <svg class="hero-arrow prev" width="24" height="46" viewBox="0 0 24 46"><path d="M22 1 1 23l21 22" fill="none" stroke="#fff" stroke-width="1.3"/></svg>
  <div class="hero-copy">
    <h1 class="hero-title">RETIREMENT PLANS</h1>
    <p class="hero-text">Lorem ipsum dolor sit amet, consectetur adipiscing elit. Etiam<br>ante massa, consectetur vel rhoncus a eget.</p>
  </div>
  <svg class="hero-arrow next" width="24" height="46" viewBox="0 0 24 46"><path d="M2 1l21 22L2 45" fill="none" stroke="#fff" stroke-width="1.3"/></svg>
</section>

<section class="steps">
  <div class="container">
    <div class="step"><h2 class="heading step-title">IDENTIFY</h2><p class="step-note">Lorem ipsum dolor sit amet consectetur.</p><div class="step-photo photo-money" role="img" aria-label="Photo of banknotes, a pen and financial charts"></div></div>
    <div class="step"><h2 class="heading step-title">PLAN</h2><p class="step-note">Lorem ipsum dolor sit amet consectetur.</p><div class="step-photo photo-laptop" role="img" aria-label="Photo of a laptop keyboard with reading glasses"></div></div>
    <div class="step"><h2 class="heading step-title">RETIRE</h2><p class="step-note">Lorem ipsum dolor sit amet consectetur.</p><div class="step-photo photo-hammock" role="img" aria-label="Photo of a hammock on a porch"></div></div>
  </div>
</section>

<section class="features">
  <h2 class="heading section-title">FEATURES</h2>
  <div class="container feature-grid">
    <div class="feature">
      <div class="feature-icon"><svg width="14" height="18" viewBox="0 0 14 18"><text x="7" y="15" text-anchor="middle" font-family="Arimo" font-weight="700" font-size="17" fill="#fff">$</text></svg></div>
      <p>Identify and project your retirement needs and expectations including basic living expenses, housing costs, recreation, big ticket non-recurring items, medical and nursing home care.</p>
    </div>
    <div class="feature">
      <div class="feature-icon"><svg width="18" height="14" viewBox="0 0 18 14"><ellipse cx="9" cy="8" rx="7" ry="5" fill="#fff"/><rect x="5" y="11" width="2" height="3" fill="#fff"/><rect x="11" y="11" width="2" height="3" fill="#fff"/></svg></div>
      <p>Identify and project all your sources of retirement income including retirement savings, other savings, pension plans, Social Security, life insurance and working part-time during retirement for a period of time.</p>
    </div>
    <div class="feature">
      <div class="feature-icon"><svg width="17" height="16" viewBox="0 0 17 16"><path d="M8.5 1 1 8h2v7h4v-4h3v4h4V8h2z" fill="#fff"/></svg></div>
      <p>Strategize tapping into the equity of your real estate including swapping your primary residence for a different home or retirement area, or selling and renting.</p>
    </div>
    <div class="feature">
      <div class="feature-icon"><svg width="18" height="16" viewBox="0 0 18 16"><path d="M2 2c0 6 2 9 6 13V9C6 8 4 6 2 2zM16 2c0 6-2 9-6 13V9c2-1 4-3 6-7z" fill="#fff"/></svg></div>
      <p>Save your work so you can return, revisit and edit your retirement plan at a later date.</p>
    </div>
  </div>
</section>

<section class="join">
  <div class="signup-card">
    <h2 class="signup-head">SIGN UP</h2>
    <div class="signup-body">
      <div class="field">Your Name</div>
      <div class="field">Email Address</div>
      <div class="submit">Sign Up</div>
    </div>
    <ul class="signup-perks">
      <li><svg width="8" height="7" viewBox="0 0 8 7"><path d="M1 3.5 3 6l4-5" fill="none" stroke="#fff" stroke-width="1.6"/></svg>Only $19.99 For a One Year Membership</li>
      <li><svg width="8" height="7" viewBox="0 0 8 7"><path d="M1 3.5 3 6l4-5" fill="none" stroke="#fff" stroke-width="1.6"/></svg>Only $9.99 Per Year After That</li>
    </ul>
  </div>
  <div class="video">
    <div class="video-frame" role="img" aria-label="Video still of two wooden chairs on a lawn facing the sea">
      <svg class="video-play" width="32" height="32" viewBox="0 0 32 32"><circle cx="16" cy="16" r="15" fill="rgba(255,255,255,.15)" stroke="#fff" stroke-width="1.5"/><path d="M13 10v12l9-6z" fill="#fff"/></svg>
    </div>
    <div class="video-bar">
      <svg width="6" height="6" viewBox="0 0 6 6"><path d="M0 0v6l6-3z" fill="#444"/></svg>
      <div class="track"></div><span>3:47 / 9:29</span>
      <svg width="7" height="6" viewBox="0 0 7 6"><path d="M0 2h2l2-2v6L2 4H0z" fill="#444"/></svg>
      <div class="vol"></div>
    </div>
  </div>
</section>

<section class="testimonials">
  <h2 class="heading section-title">TESTIMONIALS</h2>
  <div class="container quote-row">
    <figure class="quote"><blockquote class="bubble">This site is a great place to get a handle on your retirement strategy.</blockquote><figcaption class="author">Chris, <span>New Jersey</span></figcaption></figure>
    <figure class="quote"><blockquote class="bubble">It's the only retirement projection tool for the average user that puts it all together.</blockquote><figcaption class="author">Jim, <span>New York</span></figcaption></figure>
    <figure class="quote"><blockquote class="bubble">I can see professionals using this site to validate their existing retirement plans.</blockquote><figcaption class="author">Jim, <span>New Jersey</span></figcaption></figure>
  </div>
</section>

<footer class="site-footer">
  <p>Copyright © 2013 Maplecrest Harborline, Inc. All rights reserved.</p>
  <p>Terms and Conditions &nbsp;|&nbsp; Privacy Policy</p>
</footer>

</body>
</html>
```